Groovy little Insurance brokerage needs a new look

We have a new logo, but need to work out how to make it work for us!
We are a small insurance broking firm (three staff with different focus and styles), with lots of energy, experience and enthusiasm. A focus on both commercial and domestic market. We would like our cards to show a fresh look - while veering away from the 'run of the mill' insurance industry (often dull) approach.
Updates

Thanks to all for your concepts.

Had some great ideas come back, now just the process of picking which one is going to work best for us...
Will advise when we've had an opportunity to review.

Thanks!
From the team at
Kestrel Dunmore Insurance Brokers

Thanks SO much to all of your for your great designs.  Now just a process of sorting out the favorites.  If yours is eliminated, just want to say a collective thank you for your efforts!

Industry/Entity Type

Business

```html
<!DOCTYPE html>
<html lang="en">
<head>
<meta charset="utf-8">
<title>Kestrel Dunmore Insurance Brokers – Business Card</title>
<link rel="stylesheet" href="https://fonts.googleapis.com/css2?family=Open+Sans:wght@400;600;700&display=swap">
<style>
  :root {
    --paper: #f3f3f3;
    --paper-edge: #e4e4e4;
    --ink: #113a3f;
    --ink-soft: #1d4a50;
    --brand-teal: #1aa3b8;
    --band-center: #0b6e7b;
    --band-edge: #052a2f;
    --band-rule: #0a1e22;
    --band-text: #ffffff;
  }
  * { margin: 0; padding: 0; box-sizing: border-box; }
  html, body { width: 1200px; height: 734px; overflow: hidden; background: #ffffff; }
  .card {
    position: relative;
    width: 1200px;
    height: 734px;
    overflow: hidden;
    background: radial-gradient(ellipse at 55% 35%, #fafafa 0%, var(--paper) 55%, var(--paper-edge) 100%);
    font-family: "Open Sans", Arial, sans-serif;
    color: var(--ink);
  }
  .identity { position: absolute; left: 792px; top: 78px; }
  .identity__name { font-size: 58px; font-weight: 400; line-height: 1; letter-spacing: 0.5px; }
  .identity__role { font-size: 28px; font-weight: 400; line-height: 1.1; margin-top: 2px; color: var(--ink-soft); }

  .brand { position: absolute; left: 54px; top: 245px; display: flex; align-items: center; gap: 18px; }
  .brand__mark { width: 104px; height: 100px; background: var(--brand-teal); }
  .brand__name { font-size: 30px; font-weight: 700; line-height: 1.15; color: var(--ink); width: 330px; }

  .contact { position: absolute; left: 802px; top: 348px; list-style: none; }
  .contact__item { display: flex; align-items: flex-start; height: 34px; font-size: 27px; line-height: 34px; }
  .contact__icon { width: 34px; height: 34px; margin-right: 13px; flex: none; }
  .contact__icon svg { width: 34px; height: 34px; display: block; }
  .contact__text--indent { margin-left: 47px; }

  .band {
    position: absolute; left: 0; top: 584px; width: 1200px; height: 150px;
    background: radial-gradient(ellipse at 45% 45%, var(--band-center) 0%, #09545e 45%, var(--band-edge) 100%);
    border-top: 3px solid var(--band-rule);
  }
  .band__tagline {
    position: absolute; left: 0; width: 1152px; top: 36px;
    text-align: center; color: var(--band-text); font-size: 21px; line-height: 29px;
  }
</style>
</head>
<body>
<div class="card">
  <div class="identity">
    <h1 class="identity__name">Rowan Keble</h1>
    <p class="identity__role">Marketing Manager</p>
  </div>

  <div class="brand">
    <div class="brand__mark"></div>
    <p class="brand__name">Kestrel Dunmore Insurance Brokers</p>
  </div>

  <ul class="contact">
    <li class="contact__item">
      <span class="contact__icon"><svg viewBox="0 0 34 34" fill="none" stroke="#113a3f" stroke-width="1.8"><path d="M4 16 L17 5 L30 16"/><rect x="8" y="15" width="18" height="14"/><rect x="14" y="21" width="6" height="8"/><rect x="10" y="17" width="4" height="4"/></svg></span>
      <span>418 Harbour Avenue</span>
    </li>
    <li class="contact__item"><span class="contact__text--indent">Lakeview City 60218</span></li>
    <li class="contact__item">
      <span class="contact__icon"><svg viewBox="0 0 34 34" fill="none" stroke="#113a3f" stroke-width="1.8"><path d="M5 12 Q17 3 29 12 L26 15 L22 13 L22 10 Q17 8 12 10 L12 13 L8 15 Z"/><rect x="7" y="16" width="20" height="13" rx="3"/><circle cx="17" cy="22" r="3.5"/></svg></span>
      <span>+(000) 555 01927</span>
    </li>
    <li class="contact__item">
      <span class="contact__icon"><svg viewBox="0 0 34 34" fill="none" stroke="#113a3f" stroke-width="1.8"><rect x="6" y="2" width="22" height="30" rx="3"/><rect x="9" y="5" width="16" height="12"/><path d="M9 21 H25 M9 25 H25 M14 19 V29 M20 19 V29"/></svg></span>
      <span>+ (000) 555 018 342</span>
    </li>
    <li class="contact__item">
      <span class="contact__icon"><svg viewBox="0 0 34 34" fill="none" stroke="#113a3f" stroke-width="1.8"><rect x="4" y="9" width="26" height="17"/><path d="M4 9 L17 19 L30 9 M4 26 L13 16 M30 26 L21 16"/></svg></span>
      <span>rowan@kdib.com</span>
    </li>
    <li class="contact__item">
      <span class="contact__icon"><svg viewBox="0 0 34 34" fill="none" stroke="#113a3f" stroke-width="1.8"><circle cx="17" cy="17" r="14"/><ellipse cx="17" cy="17" rx="6" ry="14"/><path d="M3 17 H31 M6 9 H28 M6 25 H28"/></svg></span>
      <span>www.kdib.com</span>
    </li>
  </ul>

  <div class="band">
    <p class="band__tagline">We are a small insurance broking firm<br>(three staff with different focus and styles), with lots of energy,<br>experience and enthusiasm</p>
  </div>
</div>
</body>
</html>
```